Word Templates for Green Energy Consulting Company

Please see attached brief. This is what we'd like. Please note that we have also launched a PowerPoint template project and we want the two designs to be consistent. We encourage designers to submit to both contests. PowerPoint project is here: https://www.plintorava.com/manage-project/brief/5183620

Font styles to use
Serif
Sans Serif

```html
<!DOCTYPE html>
<html lang="en">
<head>
<meta charset="utf-8">
<title>Verdale Group – Word Template Set</title>
<link href="https://fonts.googleapis.com/css2?family=Montserrat:wght@400;500;600;700&family=Open+Sans:wght@400;600;700&family=Lora:wght@400&display=swap" rel="stylesheet">
<style>
:root{
  --stage:#7b7b7b;
  --navy:#1d2e4f;
  --blue:#1c6fb5;
  --sky:#3a9ad9;
  --green:#3d8b2a;
  --lime:#8cc63f;
  --ink:#4a4a4a;
  --dark:#2a2a2a;
  --rule:#1d2e4f;
}
*{box-sizing:border-box;margin:0;padding:0}
html,body{width:1200px;height:2582px;overflow:hidden}
body{background:var(--stage);position:relative;font-family:"Open Sans",Arial,sans-serif}
.page{position:absolute;width:334px;height:472px;background:#fff;overflow:hidden;box-shadow:0 2px 6px rgba(0,0,0,.35)}
.c1{left:82px}.c2{left:433px}.c3{left:781px}
.r1{top:78px}.r2{top:568px}.r3{top:1056px}.r4{top:1540px}.r5{top:2032px}

/* running header / footer */
.hdr-brand{position:absolute;left:14px;top:9px;font:700 5.5px "Montserrat",sans-serif;color:var(--navy);display:flex;align-items:center;gap:3px}
.hdr-brand i{display:block;width:5px;height:5px;background:var(--green)}
.hdr-title{position:absolute;right:14px;top:10px;font:600 4.5px "Montserrat",sans-serif;color:var(--dark)}
.ftr-rule{position:absolute;left:0;right:0;top:452px;height:2px;background:linear-gradient(90deg,var(--sky) 0 22%,var(--navy) 22%)}
.ftr-note{position:absolute;left:12px;top:457px;font-size:4px;color:#555}
.ftr-date{position:absolute;left:284px;top:456px;font-size:4px;color:#555}
.ftr-num{position:absolute;right:10px;top:455px;width:17px;height:7px;background:var(--navy);color:#fff;font-size:4px;text-align:center;line-height:7px}

/* type */
.h1{position:absolute;left:37px;font:500 9.5px/1.15 "Montserrat",sans-serif;color:var(--dark);text-transform:uppercase}
.h1.big{font-size:11px}
.h2{position:absolute;font:500 7.5px/1.15 "Montserrat",sans-serif;color:var(--dark);text-transform:uppercase}
.h3{position:absolute;font:700 6px/1.3 "Open Sans",sans-serif;color:var(--dark)}
.t{position:absolute;font-size:5.1px;line-height:1.27;color:var(--ink);overflow:hidden}
.l{left:37px;width:127px}
.r{left:168px;width:129px}
.w{left:37px;width:260px}
.ph{position:absolute}

/* covers */
.cover-brand{position:absolute;left:23px;top:34px;display:flex;align-items:center;gap:5px}
.cover-brand b{font:700 11px "Montserrat",sans-serif;color:var(--navy)}
.cover-brand i{display:block;width:9px;height:9px;background:var(--green)}
.cover-tag{position:absolute;left:37px;top:48px;font:400 4.5px "Montserrat",sans-serif;color:var(--green)}
.cover-title{position:absolute;left:23px;top:78px;font:600 23px/1.02 "Montserrat",sans-serif;color:var(--navy)}
.cover-lede{position:absolute;left:23px;top:134px;width:82px;font:400 5.2px/1.35 "Lora",serif;color:#444}
.cover-art{position:absolute;left:0;top:0}

/* contents */
.toc{position:absolute;left:37px;top:84px;width:258px;list-style:none}
.toc li{display:flex;font-size:5px;line-height:9.55px;color:#333}
.toc .n{flex:none}
.toc .d{flex:1;border-bottom:1px dotted #777;margin:0 1px 3px}
.toc .lv1 .n{width:13px}
.toc .lv2{padding-left:13px}.toc .lv2 .n{width:17px}
.toc .lv3{padding-left:30px}.toc .lv3 .n{width:19px}

/* back cover */
.back-name{position:absolute;left:0;right:0;top:328px;text-align:center;font:700 15px "Montserrat",sans-serif;color:var(--navy)}
.back-tag{position:absolute;left:30px;right:30px;top:350px;display:flex;align-items:center;gap:5px;font:400 6px "Montserrat",sans-serif;color:var(--green)}
.back-tag::before,.back-tag::after{content:"";flex:1;height:1px;background:var(--green)}
.contact{position:absolute;left:176px;top:404px;list-style:none;font:400 4.6px/8px "Lora",serif;color:#333}
.contact li{display:flex;align-items:center;gap:6px;margin-left:-10px}
.contact svg{width:5px;height:5px}
</style>
</head>
<body>

<!-- Cover A -->
<section class="page c1 r1">
  <svg class="cover-art" width="334" height="472" viewBox="0 0 334 472" role="img" aria-label="Grass globe with a solar panel under a beam of light and clouds, set in a blue sky">
    <defs>
      <linearGradient id="skyA" x1="0" y1="0" x2="0" y2="1">
        <stop offset="0" stop-color="#1d2e4f"/><stop offset=".45" stop-color="#1c6fb5"/><stop offset=".8" stop-color="#2c9ccf"/><stop offset="1" stop-color="#2a7f6a"/>
      </linearGradient>
    </defs>
    <polygon points="0,405 145,165 182,280 334,12 334,472 0,472" fill="url(#skyA)"/>
    <polygon points="262,0 334,0 334,6 150,330" fill="#dff0cf" opacity=".6"/>
    <polyline points="0,400 145,158 182,273 334,4" fill="none" stroke="#3d8b2a" stroke-width="4"/>
  </svg>
  <div class="cover-brand"><i></i><b>Verdale Group</b></div>
  <div class="cover-tag">Clear Thinking for Energy</div>
  <h1 class="cover-title">LOREM IPSUM<br>TITLE TEXT</h1>
  <p class="cover-lede">Lorem ipsum dolor sit amet, consectetur adipiscing elit, sed do eiusmod tempor incididunt ut labore et dolore magna aliqua. Tristique senectus et netus et malesuada fames ac.</p>
</section>

<!-- Cover B -->
<section class="page c2 r1">
  <svg class="cover-art" width="334" height="472" viewBox="0 0 334 472" role="img" aria-label="Hands working at a desk beside a small wind turbine model and a patch of grass">
    <defs>
      <linearGradient id="deskB" x1="0" y1="0" x2="1" y2="1">
        <stop offset="0" stop-color="#6e6a63"/><stop offset=".5" stop-color="#a7a096"/><stop offset="1" stop-color="#d9d5ce"/>
      </linearGradient>
    </defs>
    <polygon points="0,405 145,165 182,280 334,12 334,472 0,472" fill="url(#deskB)"/>
    <polygon points="200,0 334,0 334,12 182,280 145,165 0,405 0,430" fill="#1d2e4f" opacity="0"/>
    <polygon points="334,12 182,280 190,300 334,60" fill="#1d2e4f"/>
    <polygon points="145,165 0,405 0,472 40,472" fill="#1c6fb5" opacity=".85"/>
    <polyline points="0,400 145,158 182,273 334,4" fill="none" stroke="#3d8b2a" stroke-width="4"/>
    <line x1="200" y1="0" x2="200" y2="40" stroke="#ccc" stroke-width=".6"/>
  </svg>
  <div class="cover-brand"><i></i><b>Verdale Group</b></div>
  <div class="cover-tag">Clear Thinking for Energy</div>
  <h1 class="cover-title">LOREM IPSUM<br>TITLE TEXT</h1>
  <p class="cover-lede">Lorem ipsum dolor sit amet, consectetur adipiscing elit, sed do eiusmod tempor incididunt ut labore et dolore magna aliqua. Tristique senectus et netus et malesuada fames ac.</p>
</section>

<!-- Cover C -->
<section class="page c3 r1">
  <svg class="cover-art" width="334" height="472" viewBox="0 0 334 472" role="img" aria-label="Grey-toned grass globe with a solar panel and clouds">
    <defs>
      <radialGradient id="greyC" cx=".55" cy=".5" r=".7">
        <stop offset="0" stop-color="#d6d6d6"/><stop offset=".6" stop-color="#ececec"/><stop offset="1" stop-color="#f7f7f7"/>
      </radialGradient>
    </defs>
    <rect width="334" height="472" fill="url(#greyC)"/>
    <polygon points="0,48 0,200 110,48" fill="#1d2e4f"/>
    <polyline points="0,206 115,44" fill="none" stroke="#3d8b2a" stroke-width="3"/>
    <polygon points="334,300 334,472 218,472 270,380 300,410" fill="#1c5a9a"/>
    <polygon points="334,300 300,410 270,380 218,472 228,472 270,392 302,420 334,330" fill="#1d2e4f"/>
    <polyline points="334,296 300,404 270,374 212,472" fill="none" stroke="#3d8b2a" stroke-width="3"/>
  </svg>
  <div style="position:absolute;left:0;right:0;top:318px;text-align:center;font:700 16px 'Montserrat',sans-serif;color:var(--navy)">Verdale Group</div>
</section>

<!-- Contents -->
<section class="page c1 r2">
  <div class="hdr-brand"><i></i>Verdale Group</div><div class="hdr-title">TITLE TEXT</div>
  <h2 class="h1" style="top:60px">TABLE OF CONTENT</h2>
  <ol class="toc">
    <li class="lv1"><span class="n">1.</span>Introduction<span class="d"></span>01</li>
    <li class="lv2"><span class="n">1.1</span>Overview<span class="d"></span>02</li>
    <li class="lv3"><span class="n">1.1.1</span>Lorem ipsum dolor sit?<span class="d"></span>02</li>
    <li class="lv3"><span class="n">1.1.2</span>Lorem ipsum dolor sit amet ?<span class="d"></span>02</li>
    <li class="lv3"><span class="n">1.1.3</span>Lorem ipsum dolor<span class="d"></span>02</li>
    <li class="lv2"><span class="n">1.2</span>Purpose<span class="d"></span>03</li>
    <li class="lv3"><span class="n">1.2.1</span>Lorem ipsum dolor sit amet?<span class="d"></span>03</li>
    <li class="lv2"><span class="n">1.3</span>How to use this FAQ guide<span class="d"></span>04</li>
    <li class="lv3"><span class="n">1.3.1</span>Lorem ipsum dolor ?<span class="d"></span>04</li>
    <li class="lv3"><span class="n">1.3.2</span>Lorem ipsum dolor sit ?<span class="d"></span>04</li>
    <li class="lv3"><span class="n">1.3.3</span>Lorem ipsum ?<span class="d"></span>04</li>
    <li class="lv1"><span class="n">2.</span>General Questions<span class="d"></span>05</li>
    <li class="lv2"><span class="n">2.1</span>Overview<span class="d"></span>05</li>
    <li class="lv3"><span class="n">2.1.1</span>Lorem ipsum dolor sit?<span class="d"></span>05</li>
    <li class="lv3"><span class="n">2.1.2</span>Lorem ipsum dolor sit amet ?<span class="d"></span>05</li>
    <li class="lv3"><span class="n">2.1.3</span>Lorem ipsum dolor<span class="d"></span>05</li>
    <li class="lv2"><span class="n">2.2</span>Purpose<span class="d"></span>06</li>
    <li class="lv3"><span class="n">2.2.1</span>Lorem ipsum dolor sit amet?<span class="d"></span>06</li>
    <li class="lv2"><span class="n">2.3</span>How to use this FAQ guide<span class="d"></span>06</li>
    <li class="lv3"><span class="n">2.3.1</span>Lorem ipsum dolor ?<span class="d"></span>06</li>
    <li class="lv3"><span class="n">2.3.2</span>Lorem ipsum dolor sit ?<span class="d"></span>06</li>
    <li class="lv3"><span class="n">2.3.3</span>Lorem ipsum ?<span class="d"></span>07</li>
    <li class="lv1"><span class="n">3.</span>General Questions<span class="d"></span>08</li>
    <li class="lv2"><span class="n">3.1</span>Overview<span class="d"></span>08</li>
    <li class="lv3"><span class="n">3.1.1</span>Lorem ipsum dolor sit?<span class="d"></span>08</li>
    <li class="lv3"><span class="n">3.1.2</span>Lorem ipsum dolor sit amet ?<span class="d"></span>08</li>
    <li class="lv3"><span class="n">3.1.3</span>Lorem ipsum dolor<span class="d"></span>08</li>
    <li class="lv2"><span class="n">3.2</span>Purpose<span class="d"></span>08</li>
    <li class="lv3"><span class="n">3.2.1</span>Lorem ipsum dolor sit amet?<span class="d"></span>08</li>
    <li class="lv2"><span class="n">3.3</span>How to use this FAQ guide<span class="d"></span>09</li>
    <li class="lv3"><span class="n">3.3.1</span>Lorem ipsum dolor ?<span class="d"></span>09</li>
    <li class="lv3"><span class="n">3.3.2</span>Lorem ipsum dolor sit ?<span class="d"></span>09</li>
    <li class="lv3"><span class="n">3.3.3</span>Lorem ipsum ?<span class="d"></span>09</li>
  </ol>
  <div class="ftr-rule"></div><div class="ftr-note">©Lorem ipsum dolor sit amet, consectetur adipiscing elit</div><div class="ftr-date">[Date]</div>
</section>

<!-- 1. Introduction -->
<section class="page c2 r2">
  <div class="hdr-brand"><i></i>Verdale Group</div><div class="hdr-title">TITLE TEXT</div>
  <h2 class="h1" style="top:60px">1. INTRODUCTION HEADING 1</h2>
  <p class="t w" style="top:78px;height:85px">Lorem ipsum dolor sit amet, consectetur adipiscing elit, sed do eiusmod tempor incididunt ut labore et dolore magna aliqua. Tristique senectus et netus et malesuada fames ac. Fringilla urna porttitor rhoncus dolor purus non enim praesent. Sed faucibus turpis in eu mi bibendum. Amet venenatis urna cursus eget nunc. Viverra nam libero justo laoreet sit amet. Faucibus purus in massa tempor nec feugiat nisl pretium. Dignissim convallis aenean et tortor. Dictum varius duis at consectetur lorem. Mauris pellentesque pulvinar pellentesque habitant morbi tristique. Amet mauris commodo quis imperdiet. Ultricies mi eget mauris pharetra et ultrices neque. A lacus vestibulum sed arcu non. Amet volutpat consequat mauris nunc. Integer feugiat scelerisque varius morbi. Vel pharetra vel turpis nunc eget lorem. Id semper risus in hendrerit gravida rutrum. Purus sit amet luctus venenatis lectus magna.</p>
  <div class="ph" role="img" aria-label="Hands holding a young green seedling in soil" style="left:35px;top:240px;width:270px;height:178px;background:radial-gradient(circle at 60% 35%,#e6e08a,#7fa23c 45%,#33501f)"></div>
  <div class="ftr-rule"></div><div class="ftr-note">©Lorem ipsum dolor sit amet, consectetur adipiscing elit</div><div class="ftr-date">[Date]</div><div class="ftr-num">01</div>
</section>

<!-- 1.1 Overview -->
<section class="page c3 r2">
  <div class="hdr-brand"><i></i>Verdale Group</div><div class="hdr-title">TITLE TEXT</div>
  <h2 class="h1" style="top:60px">1.1 OVERVIEW (SUB HEADING)</h2>
  <h3 class="h3 l" style="top:78px">1.1.1 Lorem ipsum dolor sit?</h3>
  <p class="t l" style="top:93px;height:172px">Lorem ipsum dolor sit amet, consectetur adipiscing elit, sed do eiusmod tempor incididunt ut labore et dolore magna aliqua. Tristique senectus et netus et malesuada fames ac. Fringilla urna porttitor rhoncus dolor purus non enim praesent. Sed faucibus turpis in eu mi bibendum. Amet venenatis urna cursus eget nunc. Viverra nam libero justo laoreet sit amet. Faucibus purus in massa tempor nec feugiat nisl pretium. Dignissim convallis aenean et tortor. Dictum varius duis at consectetur lorem. Mauris pellentesque pulvinar pellentesque habitant morbi tristique. Amet mauris commodo quis imperdiet. Ultricies mi eget mauris pharetra et ultrices neque. A lacus vestibulum sed arcu non. Amet volutpat consequat mauris nunc. Integer feugiat scelerisque varius morbi. Vel pharetra vel turpis nunc eget lorem. Id semper risus in hendrerit gravida rutrum. Purus sit amet luctus venenatis lectus magna.</p>
  <h3 class="h3 l" style="top:275px">1.1.2 Lorem ipsum dolor sit amet?</h3>
  <p class="t l" style="top:300px;height:140px">Lorem ipsum dolor sit amet, consectetur adipiscing elit, sed do eiusmod tempor incididunt ut labore et dolore magna aliqua. Tristique senectus et netus et malesuada fames ac. Fringilla urna porttitor rhoncus dolor purus non enim praesent. Sed faucibus turpis in eu mi bibendum. Amet venenatis urna cursus eget nunc. Viverra nam libero justo laoreet sit amet. Faucibus purus in massa tempor nec feugiat nisl pretium. Dignissim convallis aenean et tortor. Dictum varius duis at consectetur lorem. Mauris pellentesque pulvinar pellentesque habitant morbi tristique. Amet mauris commodo quis imperdiet. Ultricies mi eget mauris pharetra et ultrices neque. A lacus vestibulum sed arcu non. Amet volutpat consequat mauris nunc.</p>
  <h3 class="h3 r" style="top:78px">1.1.3 Lorem ipsum dolor</h3>
  <p class="t r" style="top:93px;height:172px">Lorem ipsum dolor sit amet, consectetur adipiscing elit, sed do eiusmod tempor incididunt ut labore et dolore magna aliqua. Tristique senectus et netus et malesuada fames ac. Fringilla urna porttitor rhoncus dolor purus non enim praesent. Sed faucibus turpis in eu mi bibendum. Amet venenatis urna cursus eget nunc. Viverra nam libero justo laoreet sit amet. Faucibus purus in massa tempor nec feugiat nisl pretium. Dignissim convallis aenean et tortor. Dictum varius duis at consectetur lorem. Mauris pellentesque pulvinar pellentesque habitant morbi tristique. Amet mauris commodo quis imperdiet. Ultricies mi eget mauris pharetra et ultrices neque. A lacus vestibulum sed arcu non. Amet volutpat consequat mauris nunc. Integer feugiat scelerisque varius morbi. Vel pharetra vel turpis nunc eget lorem. Id semper risus in hendrerit gravida rutrum. Purus sit amet luctus venenatis lectus magna.</p>
  <div class="ph r" role="img" aria-label="Glass office towers seen from below against blue sky" style="top:272px;height:170px;background:linear-gradient(160deg,#cfe3f4,#5b8fbf 55%,#23466e)"></div>
  <div class="ftr-rule"></div><div class="ftr-note">©Lorem ipsum dolor sit amet, consectetur adipiscing elit</div><div class="ftr-date">[Date]</div><div class="ftr-num">02</div>
</section>

<!-- 1.2 Purpose -->
<section class="page c1 r3">
  <div class="hdr-brand"><i></i>Verdale Group</div><div class="hdr-title">TITLE TEXT</div>
  <h2 class="h1" style="top:60px">1.2 PURPOSE (SUB HEADING)</h2>
  <h3 class="h3 l" style="top:78px">1.2.1 Lorem ipsum dolor sit amet?</h3>
  <p class="t l" style="top:104px;height:162px">Lorem ipsum dolor sit amet, consectetur adipiscing elit, sed do eiusmod tempor incididunt ut labore et dolore magna aliqua. Tristique senectus et netus et malesuada fames ac. Fringilla urna porttitor rhoncus dolor purus non enim praesent. Sed faucibus turpis in eu mi bibendum. Amet venenatis urna cursus eget nunc. Viverra nam libero justo laoreet sit amet. Faucibus purus in massa tempor nec feugiat nisl pretium. Dignissim convallis aenean et tortor. Dictum varius duis at consectetur lorem. Mauris pellentesque pulvinar pellentesque habitant morbi tristique. Amet mauris commodo quis imperdiet. Ultricies mi eget mauris pharetra et ultrices neque. A lacus vestibulum sed arcu non. Amet volutpat consequat mauris nunc. Integer feugiat scelerisque varius morbi. Vel pharetra vel turpis nunc eget lorem. Id semper risus in hendrerit gravida rutrum. Purus sit amet luctus venenatis lectus magna.</p>
  <p class="t r" style="top:80px;height:180px">luctus venenatis lectus magna. Lorem ipsum dolor sit amet, consectetur adipiscing elit, sed do eiusmod tempor incididunt ut labore et dolore magna aliqua. Tristique senectus et netus et malesuada fames ac. Fringilla urna porttitor rhoncus dolor purus non enim praesent. Sed faucibus turpis in eu mi bibendum. Amet venenatis urna cursus eget nunc. Viverra nam libero justo laoreet sit amet. Faucibus purus in massa tempor nec feugiat nisl pretium. Dignissim convallis aenean et tortor. Dictum varius duis at consectetur lorem. Mauris pellentesque pulvinar pellentesque habitant morbi tristique. Amet mauris commodo quis imperdiet. Ultricies mi eget mauris pharetra et ultrices neque. A lacus vestibulum sed arcu non. Amet volutpat consequat mauris nunc. Integer feugiat scelerisque varius morbi. Vel pharetra vel turpis nunc eget lorem. Id semper risus in hendrerit gravida rutrum. Purus sit amet luctus venenatis lectus magna.</p>
  <div class="ph" role="img" aria-label="Hands holding a young green seedling in soil" style="left:35px;top:282px;width:263px;height:161px;background:radial-gradient(circle at 60% 35%,#e6e08a,#7fa23c 45%,#33501f)"></div>
  <div class="ftr-rule"></div><div class="ftr-note">©Lorem ipsum dolor sit amet, consectetur adipiscing elit</div><div class="ftr-date">[Date]</div><div class="ftr-num">03</div>
</section>

<!-- 1.3 How to use -->
<section class="page c2 r3">
  <div class="hdr-brand"><i></i>Verdale Group</div><div class="hdr-title">TITLE TEXT</div>
  <h2 class="h1" style="top:60px">1.3 HOW TO USE THIS FAQ GUIDE (SUB HEADING)</h2>
  <h3 class="h3 l" style="top:78px">1.3.1 Lorem ipsum dolor</h3>
  <p class="t l" style="top:93px;height:128px">Lorem ipsum dolor sit amet, consectetur adipiscing elit, sed do eiusmod tempor incididunt ut labore et dolore magna aliqua. Tristique senectus et netus et malesuada fames ac. Fringilla urna porttitor rhoncus dolor purus non enim praesent. Sed faucibus turpis in eu mi bibendum. Amet venenatis urna cursus eget nunc. Viverra nam libero justo laoreet sit amet. Faucibus purus in massa tempor nec feugiat nisl pretium. Dignissim convallis aenean et tortor. Dictum varius duis at consectetur lorem. Mauris pellentesque pulvinar pellentesque habitant morbi tristique. Amet mauris commodo quis imperdiet.</p>
  <h3 class="h3 l" style="top:224px">1.3.2 Lorem ipsum dolor sit</h3>
  <p class="t l" style="top:238px;height:96px">Lorem ipsum dolor sit amet, consectetur adipiscing elit, sed do eiusmod tempor incididunt ut labore et dolore magna aliqua. Tristique senectus et netus et malesuada fames ac. Fringilla urna porttitor rhoncus dolor purus non enim praesent. Sed faucibus turpis in eu mi bibendum. Amet venenatis urna cursus eget nunc. Viverra nam libero justo laoreet sit amet. Faucibus purus in massa tempor nec feugiat nisl pretium. Dignissim convallis aenean et tortor. Dictum varius duis at consectetur lorem.</p>
  <div class="ph l" role="img" aria-label="Physiotherapist assisting a patient with a shoulder exercise" style="top:350px;height:93px;background:linear-gradient(135deg,#e9eef2,#9fb4c6 60%,#3f6a92)"></div>
  <div class="ph r" role="img" aria-label="Nurse helping an older woman on an exercise bike" style="top:77px;height:155px;background:linear-gradient(135deg,#dde3e8,#a9b6c2 55%,#4d6a8a)"></div>
  <h3 class="h3 r" style="top:243px">1.3.3 Lorem ipsum</h3>
  <p class="t r" style="top:258px;height:176px">Lorem ipsum dolor sit amet, consectetur adipiscing elit, sed do eiusmod tempor incididunt ut labore et dolore magna aliqua. Tristique senectus et netus et malesuada fames ac. Fringilla urna porttitor rhoncus dolor purus non enim praesent. Sed faucibus turpis in eu mi bibendum. Amet venenatis urna cursus eget nunc. Viverra nam libero justo laoreet sit amet. Faucibus purus in massa tempor nec feugiat nisl pretium. Dignissim convallis aenean et tortor. Dictum varius duis at consectetur lorem. Mauris pellentesque pulvinar pellentesque habitant morbi tristique. Amet mauris commodo quis imperdiet. Ultricies mi eget mauris pharetra et ultrices neque. A lacus vestibulum sed arcu non. Amet volutpat consequat mauris nunc. Integer feugiat scelerisque varius morbi. Vel pharetra vel turpis nunc eget lorem. Id semper risus in hendrerit gravida rutrum. Purus sit amet luctus venenatis lectus magna.</p>
  <div class="ftr-rule"></div><div class="ftr-note">©Lorem ipsum dolor sit amet, consectetur adipiscing elit</div><div class="ftr-date">[Date]</div><div class="ftr-num">04</div>
</section>

<!-- 2 General question -->
<section class="page c3 r3">
  <div class="hdr-brand"><i></i>Verdale Group</div><div class="hdr-title">TITLE TEXT</div>
  <h2 class="h1 big" style="top:58px">2 GENERAL QUESTION (HEADING 2)</h2>
  <h2 class="h2" style="left:37px;top:86px">2.1 OVERVIEW (SUB HEADING)</h2>
  <h3 class="h3 l" style="top:102px">2.1.1 Lorem ipsum dolor sit?</h3>
  <p class="t l" style="top:117px;height:124px">Lorem ipsum dolor sit amet, consectetur adipiscing elit, sed do eiusmod tempor incididunt ut labore et dolore magna aliqua. Tristique senectus et netus et malesuada fames ac. Fringilla urna porttitor rhoncus dolor purus non enim praesent. Sed faucibus turpis in eu mi bibendum. Amet venenatis urna cursus eget nunc. Viverra nam libero justo laoreet sit amet. Faucibus purus in massa tempor nec feugiat nisl pretium. Dignissim convallis aenean et tortor. Dictum varius duis at consectetur lorem. Mauris pellentesque pulvinar pellentesque habitant morbi tristique. Amet mauris commodo quis imperdiet.</p>
  <h3 class="h3 l" style="top:248px">2.1.2 Lorem ipsum dolor sit amet?</h3>
  <p class="t l" style="top:274px;height:96px">Lorem ipsum dolor sit amet, consectetur adipiscing elit, sed do eiusmod tempor incididunt ut labore et dolore magna aliqua. Tristique senectus et netus et malesuada fames ac. Fringilla urna porttitor rhoncus dolor purus non enim praesent. Sed faucibus turpis in eu mi bibendum. Amet venenatis urna cursus eget nunc. Viverra nam libero justo laoreet sit amet. Faucibus purus in massa tempor nec feugiat nisl pretium. Dignissim convallis aenean et tortor. Dictum varius duis at consectetur lorem.</p>
  <h3 class="h3 l" style="top:379px">2.1.3 Lorem ipsum dolor</h3>
  <p class="t l" style="top:395px;height:45px">Lorem ipsum dolor sit amet, consectetur adipiscing elit, sed do eiusmod tempor incididunt ut labore et dolore magna aliqua. Tristique senectus et netus et malesuada fames ac. Fringilla urna porttitor rhoncus dolor purus non enim.</p>
  <div class="ph r" role="img" aria-label="Portrait of a smiling doctor in a clinic" style="top:104px;height:103px;background:linear-gradient(135deg,#f0ece6,#c7b8a6 55%,#8aa5bf)"></div>
  <div class="ph r" role="img" aria-label="Therapist guiding a patient through an arm stretch" style="top:222px;height:103px;background:linear-gradient(135deg,#e9eef2,#9fb4c6 60%,#3f6a92)"></div>
  <div class="ph r" role="img" aria-label="Patient exercising in a rehabilitation gym" style="top:340px;height:104px;background:linear-gradient(135deg,#dde3e8,#a9b6c2 55%,#4d6a8a)"></div>
  <div class="ftr-rule"></div><div class="ftr-note">©Lorem ipsum dolor sit amet, consectetur adipiscing elit</div><div class="ftr-date">[Date]</div><div class="ftr-num">05</div>
</section>

<!-- 2.2 / 2.3 -->
<section class="page c1 r4">
  <div class="hdr-brand"><i></i>Verdale Group</div><div class="hdr-title">TITLE TEXT</div>
  <h2 class="h2 l" style="top:57px">2.2 PURPOSE (SUB HEADING)</h2>
  <h2 class="h2 r" style="top:57px">2.3 HOW TO USE THIS FAQ GUIDE (SUB HEADING)</h2>
  <h3 class="h3 l" style="top:80px">2.2.1 Lorem ipsum dolor sit amet?</h3>
  <p class="t l" style="top:106px;height:122px">Lorem ipsum dolor sit amet, consectetur adipiscing elit, sed do eiusmod tempor incididunt ut labore et dolore magna aliqua. Tristique senectus et netus et malesuada fames ac. Fringilla urna porttitor rhoncus dolor purus non enim praesent. Sed faucibus turpis in eu mi bibendum. Amet venenatis urna cursus eget nunc. Viverra nam libero justo laoreet sit amet. Faucibus purus in massa tempor nec feugiat nisl pretium. Dignissim convallis aenean et tortor. Dictum varius duis at consectetur lorem. Mauris pellentesque pulvinar pellentesque habitant morbi tristique. Amet mauris commodo quis imperdiet.</p>
  <div class="ph l" role="img" aria-label="Therapist guiding a patient through an arm stretch" style="top:232px;height:103px;background:linear-gradient(135deg,#e9eef2,#9fb4c6 60%,#3f6a92)"></div>
  <div class="ph l" role="img" aria-label="Portrait of a smiling doctor in a clinic" style="top:338px;height:105px;background:linear-gradient(135deg,#f0ece6,#c7b8a6 55%,#8aa5bf)"></div>
  <h3 class="h3 r" style="top:88px">2.3.1 Lorem ipsum dolor</h3>
  <p class="t r" style="top:103px;height:73px">Lorem ipsum dolor sit amet, consectetur adipiscing elit, sed do eiusmod tempor incididunt ut labore et dolore magna aliqua. Tristique senectus et netus et malesuada fames ac. Fringilla urna porttitor rhoncus dolor purus non enim praesent. Sed faucibus turpis in eu mi bibendum. Amet venenatis urna cursus eget nunc. Viverra nam libero justo laoreet sit amet. Faucibus purus in massa tempor nec feugiat nisl pretium. Dignissim convallis aenean et tortor.</p>
  <div class="ph r" role="img" aria-label="Nurse helping an older woman on an exercise bike" style="top:190px;height:100px;background:linear-gradient(135deg,#dde3e8,#a9b6c2 55%,#4d6a8a)"></div>
  <h3 class="h3 r" style="top:300px">2.3.2 Lorem ipsum dolor sit</h3>
  <p class="t r" style="top:316px;height:118px">Lorem ipsum dolor sit amet, consectetur adipiscing elit, sed do eiusmod tempor incididunt ut labore et dolore magna aliqua. Tristique senectus et netus et malesuada fames ac. Fringilla urna porttitor rhoncus dolor purus non enim praesent. Sed faucibus turpis in eu mi bibendum. Amet venenatis urna cursus eget nunc. Viverra nam libero justo laoreet sit amet. Faucibus purus in massa tempor nec feugiat nisl pretium. Dignissim convallis aenean et tortor. Dictum varius duis at consectetur lorem. Mauris pellentesque pulvinar pellentesque habitant morbi tristique. Amet mauris commodo quis imperdiet.</p>
  <div class="ftr-rule"></div><div class="ftr-note">©Lorem ipsum dolor sit amet, consectetur adipiscing elit</div><div class="ftr-date">[Date]</div><div class="ftr-num">06</div>
</section>

<!-- 2.3.3 -->
<section class="page c2 r4">
  <div class="hdr-brand"><i></i>Verdale Group</div><div class="hdr-title">TITLE TEXT</div>
  <h3 class="h3 w" style="top:58px">2.3.3 Lorem ipsum dolor sit amet?</h3>
  <p class="t w" style="top:74px;height:62px">Lorem ipsum dolor sit amet, consectetur adipiscing elit, sed do eiusmod tempor incididunt ut labore et dolore magna aliqua. Tristique senectus et netus et malesuada fames ac. Fringilla urna porttitor rhoncus dolor purus non enim praesent. Sed faucibus turpis in eu mi bibendum. Amet venenatis urna cursus eget nunc. Viverra nam libero justo laoreet sit amet. Faucibus purus in massa tempor nec feugiat nisl pretium. Dignissim convallis aenean et tortor. Dictum varius duis at consectetur lorem. Mauris pellentesque pulvinar pellentesque habitant morbi tristique. Amet mauris commodo quis imperdiet.</p>
  <div class="ph" role="img" aria-label="Wind turbine above solar panels under a pale blue sky" style="left:37px;top:210px;width:260px;height:222px;background:linear-gradient(180deg,#b9d3ea,#dbe8f3 60%,#7d93ac)"></div>
  <div class="ftr-rule"></div><div class="ftr-note">©Lorem ipsum dolor sit amet, consectetur adipiscing elit</div><div class="ftr-date">[Date]</div><div class="ftr-num">07</div>
</section>

<!-- 3 General question -->
<section class="page c3 r4">
  <div class="hdr-brand"><i></i>Verdale Group</div><div class="hdr-title">TITLE TEXT</div>
  <h2 class="h1 big" style="top:58px">3. GENERAL QUESTION (HEADING 3)</h2>
  <h2 class="h2" style="left:37px;top:86px">3.1 OVERVIEW (SUB HEADING)</h2>
  <h3 class="h3 l" style="top:102px">3.1.1 Lorem ipsum dolor sit?</h3>
  <p class="t l" style="top:117px;height:116px">Lorem ipsum dolor sit amet, consectetur adipiscing elit, sed do eiusmod tempor incididunt ut labore et dolore magna aliqua. Tristique senectus et netus et malesuada fames ac. Fringilla urna porttitor rhoncus dolor purus non enim praesent. Sed faucibus turpis in eu mi bibendum. Amet venenatis urna cursus eget nunc. Viverra nam libero justo laoreet sit amet. Faucibus purus in massa tempor nec feugiat nisl pretium. Dignissim convallis aenean et tortor. Dictum varius duis at consectetur lorem. Mauris pellentesque pulvinar pellentesque habitant morbi tristique.</p>
  <div class="ph l" role="img" aria-label="Hands cupping a glowing seedling in warm sunlight" style="top:236px;height:84px;background:radial-gradient(circle at 40% 40%,#f6c86a,#c9762b 50%,#5a4a2a)"></div>
  <h3 class="h3 l" style="top:328px">3.1.2 Lorem ipsum dolor sit amet?</h3>
  <p class="t l" style="top:353px;height:81px">Lorem ipsum dolor sit amet, consectetur adipiscing elit, sed do eiusmod tempor incididunt ut labore et dolore magna aliqua. Tristique senectus et netus et malesuada fames ac. Fringilla urna porttitor rhoncus dolor purus non enim praesent. Sed faucibus turpis in eu mi bibendum. Amet venenatis urna cursus eget nunc. Viverra nam libero justo laoreet sit amet. Faucibus purus in massa tempor nec feugiat nisl pretium.</p>
  <h3 class="h3 r" style="top:102px">3.1.3 Lorem ipsum dolor</h3>
  <p class="t r" style="top:117px;height:102px">Lorem ipsum dolor sit amet, consectetur adipiscing elit, sed do eiusmod tempor incididunt ut labore et dolore magna aliqua. Tristique senectus et netus et malesuada fames ac. Fringilla urna porttitor rhoncus dolor purus non enim praesent. Sed faucibus turpis in eu mi bibendum. Amet venenatis urna cursus eget nunc. Viverra nam libero justo laoreet sit amet. Faucibus purus in massa tempor nec feugiat nisl pretium. Dignissim convallis aenean et tortor. Dictum varius duis at consectetur lorem.</p>
  <h2 class="h2 r" style="top:228px">3.2 PURPOSE(SUB HEADING)</h2>
  <h3 class="h3 r" style="top:246px">3.2.1 Lorem ipsum dolor sit amet</h3>
  <p class="t r" style="top:262px;height:84px">Lorem ipsum dolor sit amet, consectetur adipiscing elit, sed do eiusmod tempor incididunt ut labore et dolore magna aliqua. Tristique senectus et netus et malesuada fames ac. Fringilla urna porttitor rhoncus dolor purus non enim praesent. Sed faucibus turpis in eu mi bibendum. Amet venenatis urna cursus eget nunc. Viverra nam libero justo laoreet sit amet. Faucibus purus in massa tempor nec feugiat nisl pretium.</p>
  <div class="ph r" role="img" aria-label="Close-up of a filled sandwich on a board" style="top:360px;height:82px;background:linear-gradient(135deg,#e8d2b0,#b07a45 55%,#5b3d25)"></div>
  <div class="ftr-rule"></div><div class="ftr-note">©Lorem ipsum dolor sit amet, consectetur adipiscing elit</div><div class="ftr-date">[Date]</div><div class="ftr-num">08</div>
</section>

<!-- 3.3 How to use -->
<section class="page c1 r5">
  <div class="hdr-brand"><i></i>Verdale Group</div><div class="hdr-title">TITLE TEXT</div>
  <h2 class="h1" style="top:60px">3.3 HOW TO USE THIS FAQ GUIDE (SUB HEADING)</h2>
  <h3 class="h3 l" style="top:88px">3.3.1 Lorem ipsum dolor?</h3>
  <p class="t l" style="top:103px;height:110px">Lorem ipsum dolor sit amet, consectetur adipiscing elit, sed do eiusmod tempor incididunt ut labore et dolore magna aliqua. Tristique senectus et netus et malesuada fames ac. Fringilla urna porttitor rhoncus dolor purus non enim praesent. Sed faucibus turpis in eu mi bibendum. Amet venenatis urna cursus eget nunc. Viverra nam libero justo laoreet sit amet. Faucibus purus in massa tempor nec feugiat nisl pretium. Dignissim convallis aenean et tortor. Dictum varius duis at consectetur lorem. Mauris pellentesque pulvinar pellentesque habitant morbi tristique.</p>
  <div class="ph l" role="img" aria-label="Hands holding a smartphone over a desk" style="top:220px;height:86px;background:linear-gradient(135deg,#f1d9c2,#c98b63 55%,#7a5b8a)"></div>
  <h3 class="h3 l" style="top:318px">3.3.2 Lorem ipsum dolor sit?</h3>
  <p class="t l" style="top:333px;height:80px">Lorem ipsum dolor sit amet, consectetur adipiscing elit, sed do eiusmod tempor incididunt ut labore et dolore magna aliqua. Tristique senectus et netus et malesuada fames ac. Fringilla urna porttitor rhoncus dolor purus non enim praesent. Sed faucibus turpis in eu mi bibendum. Amet venenatis urna cursus eget nunc. Viverra nam libero justo laoreet sit amet. Faucibus purus in massa tempor nec feugiat nisl pretium.</p>
  <p class="t l" style="top:419px;height:14px">Fringilla urna porttitor rhoncus dolor purus non enim praesent.</p>
  <p class="t r" style="top:88px;height:42px">Fringilla urna porttitor rhoncus dolor purus non enim praesent. Sed faucibus turpis in eu mi bibendum. Amet venenatis urna cursus eget nunc. Viverra nam libero justo laoreet sit amet. Faucibus purus in massa tempor nec feugiat nisl pretium.</p>
  <div class="ph r" role="img" aria-label="Palm tree on a sunny beach with cliffs" style="top:136px;height:85px;background:linear-gradient(180deg,#8fc3e6,#d8e8ee 55%,#c9a97a)"></div>
  <h3 class="h3 r" style="top:238px">3.3.3 Lorem ipsum dolor</h3>
  <p class="t r" style="top:253px;height:98px">Lorem ipsum dolor sit amet, consectetur adipiscing elit, sed do eiusmod tempor incididunt ut labore et dolore magna aliqua. Tristique senectus et netus et malesuada fames ac. Fringilla urna porttitor rhoncus dolor purus non enim praesent. Sed faucibus turpis in eu mi bibendum. Amet venenatis urna cursus eget nunc. Viverra nam libero justo laoreet sit amet. Faucibus purus in massa tempor nec feugiat nisl pretium. Dignissim convallis aenean et tortor. Dictum varius duis at consectetur lorem.</p>
  <div class="ph r" role="img" aria-label="Trader at a desk with several screens of charts" style="top:362px;height:81px;background:linear-gradient(135deg,#cfd9e4,#6d86a3 55%,#1f2f48)"></div>
  <div class="ftr-rule"></div><div class="ftr-note">©Lorem ipsum dolor sit amet, consectetur adipiscing elit</div><div class="ftr-date">[Date]</div><div class="ftr-num">09</div>
</section>

<!-- Back cover -->
<section class="page c2 r5">
  <svg class="cover-art" width="334" height="472" viewBox="0 0 334 472" aria-hidden="true">
    <defs>
      <linearGradient id="greenBack" x1="0" y1="0" x2="0" y2="1">
        <stop offset="0" stop-color="#1f7a1f"/><stop offset=".6" stop-color="#4e9f2c"/><stop offset="1" stop-color="#a6cf6b"/>
      </linearGradient>
    </defs>
    <polygon points="0,0 334,0 334,60 190,278 150,158 0,400" fill="url(#greenBack)"/>
    <polyline points="0,408 150,166 190,286 334,68" fill="none" stroke="#e8f2dd" stroke-width="1.5"/>
  </svg>
  <div class="back-name">Verdale Group</div>
  <div class="back-tag">Clear Thinking for Energy</div>
  <ul class="contact">
    <li><svg viewBox="0 0 10 10"><path d="M5 0a3.5 3.5 0 0 0-3.5 3.5C1.5 6 5 10 5 10s3.5-4 3.5-6.5A3.5 3.5 0 0 0 5 0zm0 5a1.5 1.5 0 1 1 0-3 1.5 1.5 0 0 1 0 3z" fill="#3d8b2a"/></svg>Lorem ipsum dolor sit amet</li>
    <li><svg viewBox="0 0 10 10"><path d="M2 0l2 2.5-1 1.5c.6 1.4 1.6 2.4 3 3l1.5-1L10 8l-1.5 2C4 10 0 6 0 1.5z" fill="#3d8b2a"/></svg>00 000 0000</li>
    <li><svg viewBox="0 0 10 10"><rect x="0" y="2" width="10" height="6" fill="#3d8b2a"/><path d="M0 2l5 3.5L10 2" fill="none" stroke="#fff" stroke-width=".8"/></svg>info@lorem ipsum.co.nz</li>
    <li><svg viewBox="0 0 10 10"><circle cx="5" cy="5" r="4.5" fill="none" stroke="#3d8b2a"/><path d="M.5 5h9M5 .5c-2.4 2.6-2.4 6.4 0 9M5 .5c2.4 2.6 2.4 6.4 0 9" fill="none" stroke="#3d8b2a" stroke-width=".7"/></svg>www.lorem ipsum.co.nz</li>
  </ul>
</section>

</body>
</html>
```